Financial Services Consultant Marketing Brochure

I need a marketing brochure for a financial services consulting firm that focuses on internal audit, risk management, and regulatory management. I ma a new company and am trying to make a good first impression. The brochure needs to point out my mission, target market, and products.

Target Market(s)

Financial Services companies, small to midsize banks.

Industry/Entity Type

Financial Service

Colors
ffc214
fece3e
fee18a
fcca95
faa54b
f78f20
f37122
f68e4e
f9bb94

Requirements
Must have
• Needs to be conservative, but impactful. Must use my existing logo. Must incorporate the information that is in the enclosed strategy document.
• Must be in a tri-fold format
• Address should be:
• 418 Larkfield Road
• 9th Floor
• New York, NY 10482
Nice to have
• Pictures of people interacting.
Should not have
• Any $ or references to money.

```html
<!DOCTYPE html>
<html lang="en">
<head>
<meta charset="utf-8">
<title>Kestrel Compliance Partners Tri-fold Brochure</title>
<link href="https://fonts.googleapis.com/css2?family=Roboto+Condensed:wght@300;400;700&display=swap" rel="stylesheet">
<style>
:root{
  --gold:#c99a45;
  --ink:#1e1e1e;
  --dark:#1b1715;
  --orange-1:#ffc214;
  --orange-2:#faa54b;
  --orange-3:#f78f20;
  --page:#ece9e4;
  --white:#ffffff;
}
*{box-sizing:border-box;margin:0;padding:0}
html,body{width:1200px;height:1200px;overflow:hidden;background:var(--page)}
body{font-family:"Roboto Condensed","Arial Narrow",sans-serif;color:var(--ink)}
.brochure{position:absolute;left:41px;top:189px;width:1100px;height:845px;display:flex;box-shadow:0 6px 24px rgba(0,0,0,.18)}
.panel{position:relative;height:100%;overflow:hidden}

/* Panel 1 */
.panel-mission{width:366px;background:var(--white)}
.panel-mission .inner{position:absolute;left:31px;right:22px;top:28px}
.heading{font-weight:400;color:var(--gold);font-size:32px;line-height:1;letter-spacing:.3px}
.body-copy{font-size:13px;line-height:16.5px;margin-top:9px}
.body-copy + .body-copy{margin-top:16px}
.vision-heading{margin-top:29px}
.vision-lead{font-weight:700;font-size:15px;line-height:19.5px;margin-top:14px}
.services{list-style:none;margin-top:14px}
.services li{font-size:19px;line-height:25px;position:relative;padding-left:12px}
.services li::before{content:"";position:absolute;left:0;top:10px;width:7px;height:7px;border-radius:50%;background:var(--orange-3)}
.services + .body-copy{margin-top:18px}
.photo-team{position:absolute;left:0;bottom:0;width:100%;height:254px;background:linear-gradient(135deg,#e9eef5 0%,#c9d6e6 45%,#f2ede6 100%)}

/* Panel 2 */
.panel-markets{width:364px;background:linear-gradient(180deg,#1a1614 0%,#221c18 60%,#2e2520 100%);color:var(--white);text-align:center}
.map-us{position:absolute;left:66px;top:55px;width:240px;height:136px;background:radial-gradient(ellipse at center,#4a4038 0%,#2c2520 80%);border-radius:30px 50px 40px 20px}
.markets-heading{position:absolute;top:108px;left:0;width:100%}
.markets-copy{position:absolute;top:211px;left:22px;right:22px;font-size:13px;line-height:16.5px}
.markets-copy p + p{margin-top:16px}
.contact-heading{position:absolute;top:500px;left:0;width:100%}
.wordmark{font-weight:700;letter-spacing:1px;line-height:1}
.brand-dark{position:absolute;top:570px;left:0;width:100%;font-size:24px;color:var(--white)}
.contact-band{position:absolute;left:0;bottom:0;width:100%;height:222px}
.contact-band svg.band{position:absolute;inset:0;width:100%;height:100%}
.person{position:absolute;left:20px;top:100px;text-align:left;color:var(--ink)}
.person .full-name{font-size:25px;font-weight:400;line-height:1;letter-spacing:.5px}
.person .full-name b{font-weight:700}
.person .role{font-size:10px;letter-spacing:.4px;margin-top:4px}
.contact-list{position:absolute;left:196px;top:46px;list-style:none;text-align:left;color:var(--ink)}
.contact-list li{display:flex;align-items:flex-start;gap:9px;font-size:9.6px;font-weight:700;line-height:13px;height:40px}
.contact-list svg{flex:none;width:14px;height:14px}

/* Panel 3 */
.panel-cover{width:370px;background:linear-gradient(160deg,#ffffff 0%,#f1f0ee 55%,#ffffff 100%)}
.brand-cover{position:absolute;top:60px;left:0;width:100%;text-align:center;font-size:30px;color:var(--ink)}
.cover-visual{position:absolute;left:12px;right:12px;top:140px;height:470px;background:linear-gradient(160deg,#eef0f2 0%,#d8dce0 40%,#f7c46b 75%,#f3f3f3 100%);border-radius:4px}
.cover-statement{position:absolute;top:619px;left:12px;right:12px;text-align:center;font-size:20px;line-height:25px;color:#2a2a2a}
.cover-statement em{font-weight:700}
.cover-rule{position:absolute;left:0;top:759px;width:100%;height:7px;background:var(--gold)}
.cover-footer{position:absolute;left:0;top:766px;width:100%;height:79px;background:var(--dark);display:flex;align-items:center;justify-content:center;gap:16px}
.cover-footer .line{width:96px;height:1px;background:#6b5a44}
.cover-footer .url{color:var(--gold);font-size:12.5px;letter-spacing:.4px}
</style>
</head>
<body>
<main class="brochure">

  <section class="panel panel-mission">
    <div class="inner">
      <h2 class="heading">MISSION STATEMENT</h2>
      <p class="body-copy">Kestrel Compliance Partners’ (KCP) purpose is to provide audit, risk, and regulatory expertise to financial services companies throughout the United States. Using ethics and integrity as our cornerstones and competency as our capstone, KCP provides consulting services that will ensure that our clients and the financial services industry remain viable, safe, and solvent.</p>
      <p class="body-copy">KCP strives to ensure our client’s internal audit departments are risk-based and add value, risk management practices and processes are appropriate for their risk profiles, and clients have the ability to manage the regulatory environment, adapt to regulatory changes, and remain compliant with all regulations.</p>
      <h2 class="heading vision-heading">VISION</h2>
      <p class="vision-lead">KCP will provide consulting services in three basic categories;</p>
      <ul class="services">
        <li>Internal Audit</li>
        <li>Risk Management</li>
        <li>Regulatory Environment.</li>
      </ul>
      <p class="body-copy">Internal Audit will be KCP’s primary focus and will serve as its core service. Nonetheless, KCP has the expertise and capacity to offer products in Risk Management and the Regulatory Environment.</p>
    </div>
    <div class="photo-team" role="img" aria-label="Photo of three colleagues reviewing work together at a desk with a computer"></div>
  </section>

  <section class="panel panel-markets">
    <div class="map-us" role="img" aria-label="Dark silhouette map of the United States"></div>
    <h2 class="heading markets-heading">MARKETS</h2>
    <div class="markets-copy">
      <p>KCP’s primary area of operation will be in the Mid-Atlantic and Northeast states. However, KCP has the capacity to take assignments in any state in the continental United States. KCP’s resource plan is to use, to the extent possible, local talent enabling the engagements to remain connected to the client’s location and reduce associated travel costs.</p>
      <p>KCP’s primary client base will be small and midsize community banks, credit unions, and the foreign branch operations of international banks. These banks will typically operate in the retail and/or commercial sector. KCP will accept engagements at larger banks; however, initially KCP will only focus on risk management activities associated with commercial and retail type of banking activities in these larger institutions.</p>
    </div>
    <h2 class="heading contact-heading">CONTACT US NOW</h2>
    <div class="wordmark brand-dark">KESTREL COMPLIANCE</div>
    <div class="contact-band">
      <svg class="band" viewBox="0 0 364 222" preserveAspectRatio="none" aria-hidden="true">
        <defs>
          <linearGradient id="bandFill" x1="0" y1="0" x2="0" y2="1">
            <stop offset="0" stop-color="#ffc214"/>
            <stop offset=".55" stop-color="#faa54b"/>
            <stop offset="1" stop-color="#f78f20"/>
          </linearGradient>
        </defs>
        <path d="M0 10 Q182 30 364 0 L364 222 L0 222 Z" fill="url(#bandFill)"/>
        <line x1="182" y1="38" x2="182" y2="222" stroke="#f7b040" stroke-width="1"/>
      </svg>
      <div class="person">
        <div class="full-name">MARA <b>LINDELL</b></div>
        <div class="role">MANAGING PRINCIPAL</div>
      </div>
      <ul class="contact-list">
        <li><svg viewBox="0 0 14 14"><rect x="0" y="3" width="14" height="9" fill="#1e1e1e"/><path d="M0 3 L7 8 L14 3" stroke="#faa54b" fill="none"/></svg><span>MLINDELL@KESTRELCP.COM</span></li>
        <li><svg viewBox="0 0 14 14"><path d="M3 1 L5 1 L6 4 L4.5 5.5 Q6 8.5 8.5 9.5 L10 8 L13 9 L13 11 Q12 13 10 13 Q3 11 1 4 Q1 2 3 1 Z" fill="#1e1e1e"/></svg><span>212-555-0184</span></li>
        <li><svg viewBox="0 0 14 14"><path d="M7 1 L14 7 L12 7 L12 13 L8.5 13 L8.5 9 L5.5 9 L5.5 13 L2 13 L2 7 L0 7 Z" fill="#1e1e1e"/></svg><span>418 LARKFIELD ROAD<br>NEW YORK, NY 10482, USA</span></li>
        <li><svg viewBox="0 0 14 14"><circle cx="7" cy="7" r="6" fill="none" stroke="#1e1e1e" stroke-width="1.6"/><path d="M1 7 H13 M7 1 Q3 7 7 13 M7 1 Q11 7 7 13" stroke="#1e1e1e" fill="none" stroke-width="1"/></svg><span>WWW.KESTRELCP.COM</span></li>
      </ul>
    </div>
  </section>

  <section class="panel panel-cover">
    <div class="wordmark brand-cover">KESTREL COMPLIANCE</div>
    <div class="cover-visual" role="img" aria-label="Illustration of a calculator, rising orange growth chart and a tablet showing a risk management diagram"></div>
    <p class="cover-statement">Kestrel Compliance Partners’<br>(KCP) purpose is to provide<br><em>Audit, Risk, and Regulatory expertise</em><br>to financial services companies<br>throughout the United States.</p>
    <div class="cover-rule"></div>
    <div class="cover-footer"><span class="line"></span><span class="url">WWW.KESTRELCP.COM</span><span class="line"></span></div>
  </section>

</main>
</body>
</html>
```